Need to drive pregnant women to my 3d4d ultrasound studio where i provide 4d ultrasound with hyperalistic imaging and gender reveals

Industry/Entity Type

Healthcare

Font styles to use
Decorative
Script

Requirements
Must have
• My Company name Latido de Luna 4D. EVERYTHING HAS TO BE IN SPANISH
Nice to have
• SIMPLE AND NOT TOO BUSY
Should not have
• website

```html
<!DOCTYPE html>
<html lang="es">
<head>
<meta charset="utf-8">
<title>Latido de Luna 4D – Valla publicitaria</title>
<link href="https://fonts.googleapis.com/css2?family=Archivo+Black&family=Poppins:wght@500;600&display=swap" rel="stylesheet">
<style>
  :root {
    --bg: #eef1f5;
    --pink: #ec3a84;
    --teal: #52c3b6;
    --purple: #a224ef;
    --white: #ffffff;
    --scan-light: #d9943f;
    --scan-dark: #3a1a06;
    --skin-light: #f4c9b4;
    --skin-dark: #2a1410;
  }
  * { margin: 0; padding: 0; box-sizing: border-box; }
  html, body { width: 1200px; height: 900px; overflow: hidden; background: var(--bg); }
  .billboard {
    position: absolute; left: 40px; top: 240px;
    width: 1120px; height: 420px; overflow: hidden;
    box-shadow: 0 12px 30px rgba(0,0,0,.18);
  }
  .billboard-art { position: absolute; inset: 0; }
  .headline {
    position: absolute; left: 50px; top: 34px;
    font-family: "Archivo Black", sans-serif;
    font-size: 76px; line-height: .88; color: var(--white);
    text-transform: uppercase; letter-spacing: 1px;
  }
  .services {
    position: absolute; left: 50px; top: 258px; width: 640px;
    font-family: "Poppins", sans-serif; font-weight: 500;
    font-size: 17px; line-height: 1.3; color: var(--white);
  }
  .contact {
    position: absolute; left: 50px; top: 330px;
    display: flex; align-items: center; gap: 14px;
    font-family: "Poppins", sans-serif; color: var(--white);
  }
  .contact-label { font-size: 22px; font-weight: 500; }
  .contact-icon { width: 24px; height: 24px; }
  .contact-phone { font-size: 42px; font-weight: 600; letter-spacing: 1px; }
</style>
</head>
<body>
  <section class="billboard">
    <svg class="billboard-art" viewBox="0 0 1120 420" width="1120" height="420">
      <defs>
        <radialGradient id="scanTone" cx="45%" cy="50%" r="65%">
          <stop offset="0" stop-color="var(--scan-light)"/>
          <stop offset="1" stop-color="var(--scan-dark)"/>
        </radialGradient>
        <radialGradient id="newbornTone" cx="55%" cy="55%" r="65%">
          <stop offset="0" stop-color="var(--skin-light)"/>
          <stop offset=".75" stop-color="#d99b86"/>
          <stop offset="1" stop-color="var(--skin-dark)"/>
        </radialGradient>
      </defs>
      <rect class="band-pink" x="0" y="0" width="800" height="250" fill="var(--pink)"/>
      <rect class="band-teal" x="0" y="250" width="800" height="66" fill="var(--teal)"/>
      <rect class="band-purple" x="0" y="316" width="800" height="104" fill="var(--purple)"/>
      <path class="divider-purple" d="M690,0 L732,0 Q650,210 772,420 L735,420 Q620,210 690,0 Z" fill="var(--purple)"/>
      <path class="divider-white" d="M724,0 L732,0 Q650,210 772,420 L764,420 Q642,210 724,0 Z" fill="var(--white)"/>
      <g role="img" aria-label="Foto de ultrasonido 4D del rostro de un bebé en el vientre">
        <path d="M732,0 L890,0 L890,420 L772,420 Q650,210 732,0 Z" fill="url(#scanTone)"/>
      </g>
      <g role="img" aria-label="Foto de un recién nacido dormido">
        <rect x="890" y="0" width="230" height="420" fill="url(#newbornTone)"/>
      </g>
    </svg>

    <h1 class="headline">Latido<br>de Luna<br>4D</h1>

    <p class="services">Hacemos Ultrasonido en 3D/4d/5D ,10k Y Imagenes Hyper-realistic Serviendo la area Oeste de Puerto Rico.</p>

    <div class="contact">
      <span class="contact-label">Para orientacion</span>
      <svg class="contact-icon" viewBox="0 0 24 24" aria-hidden="true">
        <path fill="#ffffff" d="M6.6 10.8a15.1 15.1 0 0 0 6.6 6.6l2.2-2.2a1 1 0 0 1 1-.25 11.4 11.4 0 0 0 3.6.57 1 1 0 0 1 1 1V20a1 1 0 0 1-1 1A17 17 0 0 1 3 4a1 1 0 0 1 1-1h3.5a1 1 0 0 1 1 1c0 1.25.2 2.45.57 3.57a1 1 0 0 1-.25 1z"/>
      </svg>
      <span class="contact-phone">787-555-0142</span>
    </div>
  </section>
</body>
</html>
```